QTR business cards

I need a Business card design for my self. I am behavior analyst owner of a new company based in Miami. We offer Applied Behavior Analysis (ABA) services to individuals with developmental disabilities.

Business

```html
<!DOCTYPE html>
<html lang="en">
<head>
<meta charset="utf-8">
<title>QTR business cards</title>
<link rel="stylesheet" href="https://fonts.googleapis.com/css2?family=Poppins:wght@400;600;700&display=swap">
<style>
  :root {
    --qtr-blue: #15508a;
    --qtr-blue-deep: #0f4378;
    --qtr-green: #4c9e3a;
    --ink-grey: #555a60;
    --card-white: #f3f3f3;
    --backdrop: #e4e2de;
  }
  * { margin: 0; padding: 0; box-sizing: border-box; }
  html, body { width: 1200px; height: 900px; overflow: hidden; }
  body {
    background: var(--backdrop);
    font-family: "Poppins", sans-serif;
    position: relative;
  }
  .card {
    position: absolute;
    width: 600px;
    height: 343px;
    border-radius: 4px;
    box-shadow: 0 6px 18px rgba(0,0,0,0.18);
    overflow: hidden;
  }
  /* Back of card */
  .card-back {
    left: 540px;
    top: 70px;
    background: var(--qtr-blue);
  }
  .card-back .brand-mark {
    position: absolute;
    left: 70px;
    top: 128px;
    display: flex;
    align-items: center;
    gap: 14px;
  }
  .brand-dot {
    width: 22px; height: 22px;
    border-radius: 50%;
    background: rgba(255,255,255,0.18);
  }
  .card-back .brand-name {
    font-weight: 700;
    font-size: 64px;
    letter-spacing: 4px;
    color: #ffffff;
    line-height: 1;
  }
  .service-list {
    position: absolute;
    left: 300px;
    top: 112px;
    list-style: none;
  }
  .service-list li {
    display: flex;
    align-items: center;
    gap: 10px;
    color: #ffffff;
    font-size: 15px;
    letter-spacing: 1.5px;
    line-height: 30px;
  }
  .tick { width: 14px; height: 14px; flex: none; }
  /* Front of card */
  .card-front {
    left: 60px;
    top: 480px;
    background: var(--card-white);
  }
  .card-front .wave {
    position: absolute;
    inset: 0;
    width: 100%;
    height: 100%;
  }
  .card-front .brand-mark {
    position: absolute;
    left: 56px;
    top: 62px;
    display: flex;
    align-items: center;
    gap: 8px;
  }
  .card-front .brand-dot {
    width: 14px; height: 14px;
    background: var(--qtr-green);
  }
  .card-front .brand-name {
    font-weight: 700;
    font-size: 40px;
    letter-spacing: 2px;
    color: var(--qtr-blue);
    line-height: 1;
  }
  .person {
    position: absolute;
    left: 250px;
    top: 64px;
  }
  .person-name {
    font-weight: 600;
    font-size: 19px;
    letter-spacing: 3px;
    color: var(--ink-grey);
  }
  .person-title {
    font-size: 12px;
    letter-spacing: 1.4px;
    color: var(--qtr-green);
    margin-top: 2px;
  }
  .contact-list {
    position: absolute;
    left: 216px;
    top: 140px;
    list-style: none;
  }
  .contact-list li {
    display: flex;
    align-items: center;
    gap: 18px;
    font-size: 12.5px;
    letter-spacing: 1.5px;
    color: var(--ink-grey);
    line-height: 28px;
  }
  .contact-icon { width: 14px; height: 14px; flex: none; }
</style>
</head>
<body>

<section class="card card-back" aria-label="Card back">
  <div class="brand-mark">
    <span class="brand-dot"></span>
    <span class="brand-name">QTR</span>
  </div>
  <ul class="service-list">
    <li><svg class="tick" viewBox="0 0 14 14"><path d="M2 7.5 L5.5 11 L12 3" fill="none" stroke="#4c9e3a" stroke-width="2.4" stroke-linecap="round" stroke-linejoin="round"/></svg>Applied Behavior Analysis</li>
    <li><svg class="tick" viewBox="0 0 14 14"><path d="M2 7.5 L5.5 11 L12 3" fill="none" stroke="#4c9e3a" stroke-width="2.4" stroke-linecap="round" stroke-linejoin="round"/></svg>Parent/Teacher Training</li>
    <li><svg class="tick" viewBox="0 0 14 14"><path d="M2 7.5 L5.5 11 L12 3" fill="none" stroke="#4c9e3a" stroke-width="2.4" stroke-linecap="round" stroke-linejoin="round"/></svg>Social Skills Training</li>
    <li><svg class="tick" viewBox="0 0 14 14"><path d="M2 7.5 L5.5 11 L12 3" fill="none" stroke="#4c9e3a" stroke-width="2.4" stroke-linecap="round" stroke-linejoin="round"/></svg>Tutoring</li>
  </ul>
</section>

<section class="card card-front" aria-label="Card front">
  <svg class="wave" viewBox="0 0 600 343" preserveAspectRatio="none" aria-hidden="true">
    <path d="M0 118 C110 138 190 238 340 290 C440 322 530 332 600 336 L600 343 L0 343 Z" fill="#4c9e3a"/>
    <path d="M0 130 C108 150 186 250 336 300 C436 330 528 338 600 343 L0 343 Z" fill="#15508a"/>
  </svg>
  <div class="brand-mark">
    <span class="brand-dot"></span>
    <span class="brand-name">QTR</span>
  </div>
  <div class="person">
    <p class="person-name">Marisol Vega, B.A.</p>
    <p class="person-title">Board Certified Asst. Behavior Analyst (BCaBA)</p>
  </div>
  <ul class="contact-list">
    <li>
      <svg class="contact-icon" viewBox="0 0 14 14"><path d="M3 1.5 L5.5 1.5 L6.5 4.5 L5 5.8 C5.8 7.6 6.8 8.6 8.4 9.3 L9.6 7.8 L12.5 8.8 L12.5 11.5 C12.5 12.2 12 12.6 11.3 12.6 C6 12.2 1.8 8 1.5 2.8 C1.5 2.1 2.2 1.5 3 1.5 Z" fill="#15508a"/></svg>
      786-555-0142
    </li>
    <li>
      <svg class="contact-icon" viewBox="0 0 14 14"><rect x="1" y="3" width="12" height="8.5" rx="1" fill="#15508a"/><path d="M1.5 3.8 L7 8 L12.5 3.8" fill="none" stroke="#f3f3f3" stroke-width="1.1"/></svg>
      m.vega.aba@qtrmail.com
    </li>
  </ul>
</section>

</body>
</html>
```